Banner Ad Designs for tick and flea products

We sell tick and flea products online and want some great banner designs for our online website to promote our tick and flea products.

The ads must be made up in both Flash and HTML5
Ads can be formatted as .JPEG or .GIF files.

Please see the following url for creative requirements
http://help.bannerloop.com/creative-requirements/

Creative licence no limits to your imagination!

Ads must be created in the following sizes:

- Banner – 468×60
- Square – 250×250
- Small Square – 200×200
- Leaderboard – 728×90
- Medium Rectangle – 300×250
- Facebook – 100×72

please view our website at www.globalcritterstore.com.au or .com to get a feel for our website.

The aim is to attract customers who want to save on tick and flea purchases for their pets (dogs and cats)

Target Market(s)

Anyone who owns a dog or cat

Industry/Entity Type

Online

Font styles to use
Sans Serif
Other font styles liked:
• creative licence on font styles

Requirements
Must have
• Must have a strong urge to entice customers to click through.

Images wording and text etc use creative lic
Nice to have
• Strong appeal to dog and cat owners and how they can save on flea and tick essentials.
Keep it simple but effective.
Be fun and playful and inviting.
Should not have
• Please do not use words like cheap - cheapest

Strobing & Flashing - Strobing, flashing backgrounds, or otherwise distracting ads are not allowed. Do not attempt to overtly distract the user from page content.

```html
<!DOCTYPE html>
<html lang="en">
<head>
<meta charset="utf-8">
<title>Give Them A Brake – Tick &amp; Flea Banner</title>
<link rel="stylesheet" href="https://fonts.googleapis.com/css2?family=Jost:wght@700&display=swap">
<style>
  :root {
    --brand-blue: #0a68c9;
    --brand-pink: #ff6fcf;
    --paper: #ffffff;
    --panel-grey: #f7f7f7;
    --cat-tone: #6e6a66;
    --dog-tone: #9a6446;
  }
  html, body {
    margin: 0;
    padding: 0;
    overflow: hidden;
    background: var(--paper);
  }
  .banner {
    position: relative;
    width: 1200px;
    height: 217px;
    overflow: hidden;
    background: var(--paper);
    font-family: "Jost", "Futura", sans-serif;
    font-weight: 700;
  }
  .headline {
    position: absolute;
    margin: 0;
    line-height: 1;
    white-space: nowrap;
    color: var(--brand-blue);
  }
  .headline-top {
    left: 231px;
    top: 82px;
    font-size: 63px;
    letter-spacing: 0.3px;
    word-spacing: 4px;
  }
  .headline-bottom {
    left: 672px;
    top: 150px;
    font-size: 64px;
    letter-spacing: 0.5px;
  }
  .accent { color: var(--brand-pink); }

  .dog-panel {
    position: absolute;
    left: 718px;
    top: 61px;
    width: 189px;
    height: 98px;
    background: var(--panel-grey);
  }
  .art-cat,
  .art-dog {
    position: absolute;
  }
  .art-cat { left: 664px; top: 101px; width: 72px; height: 51px; }
  .art-dog { left: 767px; top: 89px; width: 86px; height: 66px; }
</style>
</head>
<body>
  <main class="banner">
    <div class="dog-panel"></div>

    <p class="headline headline-top">GIVE <span class="accent">THEM</span> A</p>

    <svg class="art-cat" viewBox="0 0 72 51" role="img" aria-label="Illustration of a running grey tabby kitten">
      <rect x="0" y="0" width="72" height="51" rx="18" fill="var(--cat-tone)"/>
    </svg>

    <svg class="art-dog" viewBox="0 0 86 66" role="img" aria-label="Illustration of a running brown puppy">
      <rect x="0" y="0" width="86" height="66" rx="24" fill="var(--dog-tone)"/>
    </svg>

    <p class="headline headline-bottom">BRAKE</p>
  </main>
</body>
</html>
```